Hydrographic business needs a business card that reaches hunters and off-road enthusiasts

We need a business card for a new hydrographics company catering to customers such as hunters, off-road ATV riders and custom vehicle enthusiasts. A western theme is preferred but professional. Our service should be thought of as upper end graphic design on firearms, off road vehicles, motorcycles, etc... See www.caldorfx.com for ideas on patterns, colors, etc...

Target Market(s)

Hunters, off road enthusiasts, custom car enthusiasts, motorcycle riders...

Industry/Entity Type

Graphic Design

```html
<!DOCTYPE html>
<html lang="en">
<head>
<meta charset="utf-8">
<title>Caldor Dipcoat Studio – Business Card</title>
<link rel="stylesheet" href="https://fonts.googleapis.com/css2?family=Lobster&family=Open+Sans:wght@400;600&display=swap">
<style>
  :root {
    --page-bg: #d9c3a0;
    --frame-black: #141010;
    --back-dark: #4a1410;
    --back-mid: #6e2618;
    --front-gold: #e2b24a;
    --front-orange: #c86a22;
    --front-rust: #8e3a16;
    --brush-black: #1a1512;
    --brush-red: #a5191b;
    --name-cream: #f6e3a8;
    --title-orange: #f08a2a;
    --contact-white: #f4ead8;
    --badge-cream: #eadfc6;
  }
  * { margin: 0; padding: 0; box-sizing: border-box; }
  html, body { width: 1200px; height: 970px; overflow: hidden; }
  body {
    background: var(--page-bg);
    display: flex;
    flex-direction: column;
    align-items: center;
    justify-content: center;
    gap: 50px;
    font-family: "Open Sans", sans-serif;
  }
  .card {
    position: relative;
    width: 700px;
    height: 400px;
    overflow: hidden;
    box-shadow: 0 6px 18px rgba(60, 30, 10, 0.35);
  }
  .card-frame {
    position: absolute;
    inset: 22px;
    border: 12px solid var(--frame-black);
  }
  /* Back side */
  .card-back {
    background: radial-gradient(ellipse at 45% 40%, var(--back-mid), var(--back-dark) 80%);
  }
  .card-back .card-frame { inset: 26px; }
  .back-badge {
    position: absolute;
    left: 50%; top: 50%;
    transform: translate(-50%, -50%);
    display: flex;
    align-items: center;
    gap: 14px;
    white-space: nowrap;
  }
  .badge-dot {
    width: 22px; height: 22px;
    border-radius: 50%;
    background: var(--badge-cream);
    flex: none;
  }
  .badge-name {
    font-weight: 600;
    font-size: 30px;
    color: var(--badge-cream);
    white-space: nowrap;
  }
  /* Front side */
  .card-front {
    background: radial-gradient(ellipse at 40% 40%, var(--front-gold) 0%, var(--front-orange) 55%, var(--front-rust) 100%);
  }
  .brush-strokes { position: absolute; inset: 0; }
  .front-badge {
    position: absolute;
    left: 62px; top: 180px;
    display: flex;
    align-items: center;
    gap: 8px;
  }
  .front-badge .badge-dot { width: 14px; height: 14px; }
  .front-badge .badge-name { font-size: 16px; color: var(--badge-cream); }
  .contact-block {
    position: absolute;
    left: 318px; top: 110px;
    width: 340px;
    white-space: nowrap;
  }
  .person-name {
    font-family: "Lobster", cursive;
    font-size: 46px;
    color: var(--name-cream);
    line-height: 1.1;
  }
  .person-title {
    font-size: 14px;
    letter-spacing: 6px;
    color: var(--title-orange);
    margin-top: 10px;
  }
  .contact-line {
    font-size: 12px;
    color: var(--contact-white);
    margin-top: 12px;
  }
  .contact-line + .contact-line { margin-top: 6px; }
</style>
</head>
<body>

  <section class="card card-back" aria-label="Card back">
    <div class="card-frame"></div>
    <div class="back-badge">
      <span class="badge-dot"></span>
      <span class="badge-name">Caldor Dipcoat Studio</span>
    </div>
  </section>

  <section class="card card-front" aria-label="Card front">
    <svg class="brush-strokes" width="700" height="400" viewBox="0 0 700 400" aria-hidden="true">
      <polygon points="295,100 675,72 680,168 305,182" fill="var(--brush-black)" opacity="0.92"/>
      <polygon points="298,172 680,150 685,330 315,345" fill="var(--brush-red)" opacity="0.9"/>
    </svg>
    <div class="card-frame"></div>
    <div class="front-badge">
      <span class="badge-dot"></span>
      <span class="badge-name">Caldor Dipcoat Studio</span>
    </div>
    <div class="contact-block">
      <div class="person-name">Wade Caldor</div>
      <div class="person-title">MANAGING DIRECTOR</div>
      <div class="contact-line">512 Mesa Ridge Road 2240, Dry Creek, TX 75001</div>
      <div class="contact-line">214-555-0187 · wade@caldorfx.com · www.caldorfx.com</div>
    </div>
  </section>

</body>
</html>
```